Lumen QRX - Website

Lumen QRX is a online marketing solutions Agency, working with top partners within the industry to deliver online customers to Digital campaigns.

Our current site is www.lumenqrx-example.com (Apart from the logo, there is NOTHING we like about this site - please do not repeat anything from this site)

Specification of website:

- Modern, and light refreshing look. Corporate and neutral designs.

-Keep our logo - colour theme: Green/grey - hint of Orange/Blue

- The only text we would like on the Homepage is: Performance based online marketing specialists, driving incremental sales globally

and...

These are headings we would like people to do: Affiliate Marketing, Email marketing, Lead Generation, Social media marketing, Search Engine Marketing, Incentive Marketing (there is no need for the detailed text of these topics to be on front page, these can be linked into another page for those who seeks further info)

Images: Have images to show what we do.. keep it neat and professional/simple and stylish.

Please contact us if you have any questions at all.

Thank you for taking time our with our project!

Good luck all!

Regards

Lumen QRX
Updates

Hello Designers,

Thank you to all who have taken time out working on our project. We have been very happy with the quality and level of prompt feedback.

Unfortunately we could only choose one, and VelBoro's designed is most suited for our company branding. So, Congratulations VelBoro.

Once again, thank you all.

Kindest regards,

Lumen QRX

Target Market(s)

Clients: Fizzo, Torvik, Lunto, panelo.example, Brevard Hotel...

Industry/Entity Type

Marketing

Requirements
Must have
• User friendly
Nice to have
• We operate Internationally, so a generic feel for EU/UK/US would be ideal...
Should not have
• Should not look like www.lumenqrx-example.com

```html
<!DOCTYPE html>
<html lang="en">
<head>
<meta charset="utf-8">
<title>Lumen QRX – Performance Based Online Marketing</title>
<link href="https://fonts.googleapis.com/css2?family=Arimo:wght@400;700&display=swap" rel="stylesheet">
<style>
  :root{
    --nav-top:#5a5a5a;
    --nav-bottom:#1c1c1c;
    --pill-top:#8fd14f;
    --pill-bottom:#4f9a22;
    --green:#5f9c33;
    --green-logo:#5ea833;
    --rule:#4d8528;
    --grey-text:#707070;
    --grey-dark:#4a4a4a;
    --footer-top:#4a4a4a;
    --footer-bottom:#151515;
    --link-green:#8ed04e;
    --white:#ffffff;
  }
  *{margin:0;padding:0;box-sizing:border-box}
  html,body{width:1200px;height:608px;overflow:hidden}
  body{position:relative;font-family:"Arimo",Arial,sans-serif;background:var(--green)}

  .topnav{position:absolute;left:0;top:0;width:1200px;height:36px;
    background:linear-gradient(var(--nav-top),var(--nav-bottom))}
  .topnav a{position:absolute;top:10px;color:var(--white);font-size:12px;text-decoration:none}
  .topnav .current{left:136px;top:4px;width:81px;height:28px;border-radius:6px;
    background:linear-gradient(var(--pill-top),var(--pill-bottom));text-align:center;line-height:28px}
  .topnav .sep{position:absolute;top:11px;width:1px;height:15px;background:#111}

  .hero{position:absolute;left:0;top:36px;width:1200px;height:233px;background:var(--white);
    border:1px solid #8a8a8a;border-top:none}
  .hero-visual{position:absolute;left:431px;top:0;width:609px;height:232px;
    background:radial-gradient(ellipse at 70% 55%,#cfd6df 0%,#e6e8ea 45%,#ffffff 85%)}
  .brand{position:absolute;left:150px;top:42px;font-size:44px;font-weight:700;color:var(--green-logo);letter-spacing:-1px}
  .tagline{position:absolute;left:176px;top:146px;font-size:20px;line-height:24px;color:var(--grey-text)}
  .tagline strong{color:var(--grey-dark)}
  .tagline .q{position:absolute;font-size:34px;color:#a8a8a8;font-weight:700;line-height:34px}

  .intro{position:absolute;left:176px;top:296px;width:545px;font-size:13px;line-height:16px;color:var(--white)}
  .quote-btn{position:absolute;left:803px;top:302px;width:167px;height:40px;text-decoration:none}
  .divider{position:absolute;left:176px;top:381px;width:848px;height:1px;background:var(--rule)}

  .services{position:absolute;left:0;top:422px;list-style:none}
  .services li{position:absolute;white-space:nowrap;font-size:13px;line-height:19px;color:var(--white);padding-left:12px}
  .services li::before{content:"";position:absolute;left:0;top:6px;border-left:6px solid #1f3d10;
    border-top:4px solid transparent;border-bottom:4px solid transparent}
  .col-sep{position:absolute;top:422px;width:1px;height:37px;background:var(--rule)}

  .footer{position:absolute;left:0;top:504px;width:1200px;height:104px;
    background:linear-gradient(var(--footer-top),var(--footer-bottom));text-align:center}
  .footer-links{position:absolute;top:20px;width:100%;font-size:12px;color:#cfcfcf}
  .footer-links a{color:var(--link-green);text-decoration:none;margin:0 4px}
  .footer-links a.active{color:var(--white)}
  .copyright{position:absolute;top:45px;width:100%;font-size:10px;color:#9a9a9a}
  .powered{position:absolute;top:64px;width:100%;font-size:10px;color:#9a9a9a}
  .powered span{color:var(--link-green)}
</style>
</head>
<body>
  <nav class="topnav">
    <a class="current" href="#">Home</a>
    <a style="left:240px" href="#">About us</a><span class="sep" style="left:308px"></span>
    <a style="left:333px" href="#">What we do</a><span class="sep" style="left:417px"></span>
    <a style="left:441px" href="#">Our work</a><span class="sep" style="left:510px"></span>
    <a style="left:533px" href="#">Work with us</a><span class="sep" style="left:623px"></span>
    <a style="left:648px" href="#">Contact us</a>
  </nav>

  <header class="hero">
    <div class="hero-visual" role="img" aria-label="Faint grey world map behind a team of five business professionals standing with arms crossed"></div>
    <div class="brand">Lumen QRX</div>
    <p class="tagline">
      <span class="q" style="left:-26px;top:-4px">“</span>
      Performance Based<br>
      <strong>Online Marketing Specialists</strong>,<br>
      Driving Incremental Sales Globally
      <span class="q" style="left:312px;top:46px">”</span>
    </p>
  </header>

  <p class="intro">At Lumen QRX, we take care of every aspect of your digital marketing strategy, from planning &amp; creative to execution and acquisition. We are a proactive team focused on delivering qualified web traffic, increasing ROI for our clients and adding value with incremental sales.</p>

  <a class="quote-btn" href="#" aria-label="Get A Quote!">
    <svg width="167" height="40" viewBox="0 0 167 40">
      <defs>
        <linearGradient id="btnBlue" x1="0" y1="0" x2="0" y2="1">
          <stop offset="0" stop-color="#4db4f0"/><stop offset="1" stop-color="#0f6fb8"/>
        </linearGradient>
        <linearGradient id="btnOrange" x1="0" y1="0" x2="0" y2="1">
          <stop offset="0" stop-color="#ffc13a"/><stop offset="1" stop-color="#e07d06"/>
        </linearGradient>
      </defs>
      <rect x="12" y="4" width="153" height="32" rx="12" fill="url(#btnBlue)" stroke="#fff" stroke-width="2"/>
      <circle cx="20" cy="20" r="18" fill="url(#btnOrange)" stroke="#fff" stroke-width="2.5"/>
      <path d="M12 20 l6 6 l10 -12" fill="none" stroke="#fff" stroke-width="3.5" stroke-linecap="round" stroke-linejoin="round"/>
      <text x="48" y="26" font-family="Arimo, Arial, sans-serif" font-size="16" font-weight="700" fill="#fff">Get A Quote!</text>
    </svg>
  </a>

  <div class="divider"></div>

  <ul class="services">
    <li style="left:178px;top:0">Email Marketing</li>
    <li style="left:178px;top:19px">Lead Generation</li>
    <li style="left:384px;top:0">Incentive Marketing</li>
    <li style="left:384px;top:19px">Social media Marketing</li>
    <li style="left:605px;top:0">Search Engine Marketing</li>
    <li style="left:605px;top:19px">Affiliate Marketing</li>
  </ul>
  <span class="col-sep" style="left:343px"></span>
  <span class="col-sep" style="left:576px"></span>

  <footer class="footer">
    <p class="footer-links">
      <a class="active" href="#">Home</a> | <a href="#">About Us</a> | <a href="#">What we Do</a> | <a href="#">Our work</a> | <a href="#">Work with us</a> | <a href="#">Contact Us</a>
    </p>
    <p class="copyright">Copyright © 2010 Lumen QRX. All Rights Reserved.</p>
    <p class="powered">Powered by: <span>LUMEN QRX</span></p>
  </footer>
</body>
</html>
```